Website Landing Page for Brightfall Systems

Create a custom designed website landing page for our business. Looking for a professional upscale design that incorporates our logo and logo colors into the theme. I want a standard fixed frame website, not a constant scrolling format that seems to be the trend. To start with I'm looking for more of the graphic design part, maybe a concept or theme, I don't expect to see a finished project. Not interested in generic templates or layouts.

The name of our company is Brightfall Systems and I've attached our logo below. I'd like to have the web page have the same look and feel of our logo, as well as the colors. Our company, Brightfall Systems does system design, installation, and programming, of residential and commercial Audio/Video and Automation systems. We do home theaters, lighting and building automation, video conferencing systems, security camera installations, conference rooms, projectors, distributed audio systems, and similar Technology projects. This will be a professional services/informational website. We will not sell products on this website. This website will be used to advertise our company and communicate our services to prospective customers. Having a well designed, professional and clean website is one way we want to distinguish our company from the competition.

Here are some examples of what I consider a professional well designed website
http://www.qorlamstudio.com/Work/

Last year we had our tradlo store designed (with PixelMarket) and I'm really happy with the way it turned out. You can see it at www.HolvenGearDepot.com I consider this to be a great design and looking for the same level of quality with this new website. However, do not copy or use any part of this design in this new project. This tradlo store is completely separate from our other company Brightfall Systems. I only mention this tradlo store an an example of good work.

Reason: Still going through designs.

Reason: Still working on project and have not had time to review all designs and request revisions.

Reason: Sill going through designs and requesting revisions

Reason: still going through all the submissions we received.

Target Market(s)

People interested in Audio/Video, home theaters, home automation. We do sales, system design, and programming. We typically work on larger projects with both residential and commercial customers.

Industry/Entity Type

Business

Number of Pages Required

1 page

Requirements
Must have
• Great design elements. Please use a white background. I think white goes well with our logo colors.

```html
<!DOCTYPE html>
<html lang="en">
<head>
<meta charset="utf-8">
<title>Brightfall Systems</title>
<link rel="stylesheet" href="https://fonts.googleapis.com/css2?family=Montserrat:wght@400;500&family=Open+Sans:wght@400;600;700&family=Roboto:wght@400;500&display=swap">
<style>
  :root {
    --brand-blue: #35aede;
    --brand-blue-deep: #2d8fd0;
    --nav-blue: #3b8dd0;
    --brand-green: #8cc63f;
    --green-wash: #9ccb45;
    --teal-wash: #3a9bb0;
    --white: #ffffff;
    --ink: #0f1a0a;
  }
  * { margin: 0; padding: 0; box-sizing: border-box; }
  html, body { width: 1200px; height: 1062px; overflow: hidden; background: var(--white); }
  .page { position: relative; width: 1200px; height: 1062px; overflow: hidden; font-family: "Open Sans", sans-serif; }
  .backdrop { position: absolute; inset: 0; }

  .nav-link {
    position: absolute; top: 36px;
    font-family: "Roboto", sans-serif; font-size: 16.5px; font-weight: 400;
    color: var(--nav-blue); text-decoration: none; letter-spacing: 0.2px;
  }
  .nav-link.is-active::after {
    content: ""; position: absolute; left: 0; right: 0; bottom: -12px;
    height: 2px; background: var(--brand-green);
  }

  .brand { position: absolute; left: 463px; top: 15px; display: flex; align-items: center; gap: 18px; }
  .brand-mark { width: 93px; height: 93px; border-radius: 50%; border: 9px solid var(--brand-blue); }
  .brand-name {
    font-family: "Roboto", sans-serif; font-weight: 500; font-size: 27px;
    line-height: 29px; color: var(--brand-blue-deep); text-transform: uppercase; letter-spacing: 0.5px;
  }

  .hero-title {
    position: absolute; top: 282px; left: 0; width: 1200px; text-align: center;
    font-family: "Montserrat", sans-serif; font-weight: 400; font-size: 60px; color: var(--white);
    text-shadow: 0 2px 6px rgba(0,0,0,0.35);
  }
  .hero-lede {
    position: absolute; top: 357px; left: 200px; width: 800px; text-align: center;
    font-size: 22.5px; line-height: 25px; color: var(--white);
    text-shadow: 0 1px 4px rgba(0,0,0,0.45);
  }
  .btn {
    position: absolute; display: flex; align-items: center; justify-content: center;
    border-radius: 26px; color: var(--white); text-decoration: none;
    background: linear-gradient(#3dbbe8, #2b8fcf);
    box-shadow: 2px 4px 6px rgba(0,0,0,0.35);
  }
  .btn-contact { left: 496px; top: 427px; width: 203px; height: 52px; font-weight: 700; font-size: 17px; }
  .btn-more { left: 512px; top: 906px; width: 172px; height: 50px; font-size: 19px; gap: 8px; }

  .slider-dots { position: absolute; top: 581px; left: 542px; display: flex; gap: 10px; }
  .slider-dots span { width: 21px; height: 21px; border-radius: 50%; background: var(--white); }
  .slider-dots span.is-current { background: var(--brand-green); }

  .welcome-mark {
    position: absolute; left: 569px; top: 645px; width: 62px; height: 62px;
    border-radius: 50%; border: 5px solid var(--white);
  }
  .welcome-title {
    position: absolute; top: 711px; left: 0; width: 1200px; text-align: center;
    font-family: "Roboto", sans-serif; font-weight: 400; font-size: 44px; color: var(--ink);
  }
  .welcome-copy {
    position: absolute; top: 781px; left: 100px; width: 1000px; text-align: center;
    font-size: 16px; line-height: 25px; color: var(--white);
  }

  .site-footer {
    position: absolute; left: 0; top: 1010px; width: 1200px; height: 52px;
    background: var(--brand-blue); color: var(--white);
    display: flex; align-items: center; justify-content: center; font-size: 16.5px;
  }
  .site-footer strong { font-weight: 700; }
</style>
</head>
<body>
<div class="page">
  <svg class="backdrop" width="1200" height="1062" viewBox="0 0 1200 1062" aria-hidden="false">
    <defs>
      <linearGradient id="heroTones" x1="0" y1="0" x2="0" y2="1">
        <stop offset="0" stop-color="#b9c1c8"/>
        <stop offset="0.35" stop-color="#8e949a"/>
        <stop offset="0.6" stop-color="#5d6a3e"/>
        <stop offset="1" stop-color="#4d6a35"/>
      </linearGradient>
      <linearGradient id="roomTones" x1="0" y1="0" x2="0" y2="1">
        <stop offset="0" stop-color="#a3d04a"/>
        <stop offset="1" stop-color="#8fc23a"/>
      </linearGradient>
    </defs>
    <rect x="0" y="0" width="1200" height="720" fill="url(#heroTones)" role="img" aria-label="City skyline with office towers above a park, trees and a canal"/>
    <path d="M0 690 C200 610 400 615 600 628 C850 640 1000 690 1200 705 V1062 H0 Z" fill="var(--teal-wash)" opacity="0.85"/>
    <path d="M0 655 C250 705 450 622 600 620 C800 618 1000 690 1200 698 V1010 H0 Z" fill="url(#roomTones)" role="img" aria-label="Faint conference room with a long table and chairs"/>
    <path d="M0 68 Q600 192 1200 68 V82 Q600 204 0 82 Z" fill="var(--brand-blue)"/>
    <path d="M0 0 H1200 V66 Q600 190 0 66 Z" fill="var(--white)"/>
  </svg>

  <nav class="main-nav">
    <a class="nav-link is-active" href="#" style="left:79px">HOME</a>
    <a class="nav-link" href="#" style="left:190px">ABOUT US</a>
    <a class="nav-link" href="#" style="left:330px">SERVICES</a>
    <a class="nav-link" href="#" style="left:786px">PROJECTS</a>
    <a class="nav-link" href="#" style="left:908px">GALLERY</a>
    <a class="nav-link" href="#" style="left:1022px">CONTACT US</a>
  </nav>

  <div class="brand">
    <div class="brand-mark"></div>
    <div class="brand-name">Brightfall<br>Systems</div>
  </div>

  <h1 class="hero-title">Brightfall Systems</h1>
  <p class="hero-lede">We are a leader in the system design, installation, and programming of residential and commercial Audio/Video and Automation systems.</p>
  <a class="btn btn-contact" href="#">CONTACT US NOW</a>

  <div class="slider-dots"><span class="is-current"></span><span></span><span></span><span></span></div>

  <div class="welcome-mark"></div>
  <h2 class="welcome-title">Welcome To Brightfall Systems</h2>
  <p class="welcome-copy">Lorem Ipsum is simply dummy text of the printing and typesetting industry. Lorem Ipsum has been the industry's standard dummy text ever since the 1500s, when an unknown printer took a galley of type and scrambled it to make a type specimen book. It has survived not only five centuries, but also the leap into electronic typesetting, remaining essentially unchanged. It was popularised in the 1960s with the release of Letraset sheets containing Lorem Ipsum passages...</p>
  <a class="btn btn-more" href="#">READ MORE
    <svg width="14" height="14" viewBox="0 0 14 14" aria-hidden="true"><path d="M2 2 L7 7 L2 12 M7 2 L12 7 L7 12" fill="none" stroke="#fff" stroke-width="2"/></svg>
  </a>

  <footer class="site-footer">©&nbsp;<strong>Brightfall Systems -</strong>2017. All Rights Reserved.</footer>
</div>
</body>
</html>
```